Dermavale "polish what the seasons left you" The whole body approach to beauty, customized skincare a

I need a stronger logo design than what I have now. I currently have a small med spa in Chicago, IL. I will be expanding my brand to New York City and the Hamptons of NY. The services I provide in Chicago include; advanced medical grade skincare treatments, laser, plastic surgery and nutrition counsel. My concept is personalized skincare. Part of my philosophy is to dedicate a lot of time and make myself always available to my clients questions and concerns. To maintain integrity of the Dermavale Philosophy I do not advertise. Dermavale is an "exclusive skincare club" therefore you must be referred by an existing client or staff member in order to get an appointment. My Chicago clientele consists of young professionals competing with their peers to look their absolute best. The New York and Hamptons business has a completely different structure. It is a Mobile med spa service providing treatments at people's homes. The services provided are advanced skincare, wellness, massage, spray tan, hair and makeup. My vision for the new logo design is to exude an image that is both cutting edge, relevant, sophisticated, sexy and modern (sleek) yet practical and strong. It must be eye catching yet simplistic, aesthetically pleasing to look at and above all must promote EXCLUSIVITY! bellow I have attached my current logo design which is printed using silver and gold foil. The other is the logo on my prescription skincare products. I need to merge the two for the brand to be cohesive. I would like to print my business cards on a mirror like material where you can see your reflection. Front of card: the brand Dermavale across the front and across the bottom will be Chicago. New York. Hamptons Back of card: in a font style like writing "Dermavale is the whole body approach to beauty. customized medical grade skincare. massage. wellness counsel. By appointment only
www.dermavalewellness-example.com p: (555) 318-2406
I am open to all suggestions to make my brand as strong as possible. Please be creative and relevant. Thank you!

```html
<!DOCTYPE html>
<html lang="en">
<head>
<meta charset="utf-8">
<title>Dermavale Business Card – Front and Back</title>
<link rel="stylesheet" href="https://fonts.googleapis.com/css2?family=Arimo:wght@400;700&family=Montserrat:wght@300&display=swap">
<style>
  :root {
    --canvas: #ffffff;
    --mirror: #8fa5c0;
    --mirror-note: rgba(255, 255, 255, 0.38);
    --white: #ffffff;
    --gold: #b39a5a;
    --slate: #8b9ba3;
    --label: #8797a0;
    --crop: #111111;
    --edge: #eeeeee;
  }
  * { margin: 0; padding: 0; box-sizing: border-box; }
  html, body { width: 1200px; height: 1047px; overflow: hidden; background: var(--canvas); }
  body { position: relative; font-family: "Arimo", Helvetica, Arial, sans-serif; }

  .card { position: absolute; top: 49px; width: 497px; height: 856px; overflow: hidden; }
  .card--front { left: 65px; background: var(--mirror); }
  .card--back { left: 636px; background: var(--white); border: 1px solid var(--edge); }

  .mirror-guides { position: absolute; inset: 0; }
  .mirror-note {
    position: absolute; transform: translate(-50%, -50%);
    color: var(--mirror-note); font-size: 29px; line-height: 37px; text-align: center;
  }

  .brand-name { position: absolute; left: 0; width: 100%; text-align: center; font-weight: 700; letter-spacing: -1.5px; }
  .card--front .brand-name { top: 712px; font-size: 58px; color: var(--white); }
  .locations {
    position: absolute; top: 784px; left: 0; width: 100%; text-align: center;
    color: var(--white); font-size: 26px; letter-spacing: 0.5px;
  }

  .philosophy {
    position: absolute; top: 95px; left: 0; width: 100%; text-align: center;
    color: var(--gold); font-size: 31px; line-height: 39px; letter-spacing: 0.3px;
  }
  .philosophy strong { display: block; font-size: 36px; line-height: 44px; }

  .booking {
    position: absolute; top: 482px; left: 0; width: 100%; text-align: center; color: var(--slate);
  }
  .booking__note { font-size: 39px; letter-spacing: -2px; line-height: 46px; }
  .booking__phone { font-size: 38px; letter-spacing: 2px; line-height: 50px; }

  .card--back .brand-name { top: 712px; left: 33px; width: auto; text-align: left; font-size: 58px; color: var(--slate); }
  .brand-rule {
    position: absolute; top: 787px; left: 0; width: 100%; height: 5px;
    background: linear-gradient(to right, var(--gold) 0 68%, var(--slate) 68% 100%);
  }
  .website {
    position: absolute; top: 797px; left: 0; width: 100%; text-align: center;
    color: var(--gold); font-size: 23px; letter-spacing: 1.5px;
  }

  .crop-marks { position: absolute; inset: 0; pointer-events: none; }

  .side-label {
    position: absolute; top: 946px; transform: translateX(-50%);
    font-family: "Montserrat", Helvetica, Arial, sans-serif; font-weight: 300;
    font-size: 54px; letter-spacing: 3px; color: var(--label);
  }
  .side-label--front { left: 293px; }
  .side-label--back { left: 883px; }
</style>
</head>
<body>

<section class="card card--front" aria-label="Card front">
  <svg class="mirror-guides" width="497" height="856" viewBox="0 0 497 856" aria-hidden="true">
    <g stroke="rgba(255,255,255,0.38)" stroke-width="2" stroke-dasharray="34 46">
      <line x1="30" y1="55" x2="228" y2="400"/>
      <line x1="467" y1="55" x2="269" y2="400"/>
      <line x1="228" y1="454" x2="30" y2="800"/>
      <line x1="269" y1="454" x2="467" y2="800"/>
    </g>
  </svg>
  <p class="mirror-note" style="left:252px;top:311px">Mirror<br>Material</p>
  <p class="mirror-note" style="left:124px;top:474px">Mirror<br>Material</p>
  <p class="mirror-note" style="left:373px;top:474px">Mirror<br>Material</p>
  <p class="mirror-note" style="left:249px;top:604px">Mirror<br>Material</p>
  <p class="mirror-note" style="left:250px;top:427px">X</p>

  <p class="brand-name">Dermavale</p>
  <p class="locations">Chicago • New York • Hamptons</p>
</section>

<section class="card card--back" aria-label="Card back">
  <p class="philosophy">
    <strong>Dermavale</strong>
    is the whole body<br>
    approach to beauty.<br>
    Customized medical<br>
    grade skincare.<br>
    Massage.<br>
    Wellness counsel.
  </p>
  <div class="booking">
    <p class="booking__note">By appointment only</p>
    <p class="booking__phone">(555) 318-2406</p>
  </div>
  <p class="brand-name">Dermavale</p>
  <div class="brand-rule"></div>
  <p class="website">www.dermavalewellness-example.com</p>
</section>

<svg class="crop-marks" width="1200" height="1047" viewBox="0 0 1200 1047" aria-hidden="true">
  <g stroke="var(--crop)" stroke-width="1">
    <path d="M41 49h49M65 25v49 M538 49h49M562 25v49 M41 905h49M65 881v49 M538 905h49M562 881v49"/>
    <path d="M612 49h49M636 25v49 M1109 49h49M1133 25v49 M612 905h49M636 881v49 M1109 905h49M1133 881v49"/>
  </g>
</svg>

<p class="side-label side-label--front">FRONT</p>
<p class="side-label side-label--back">BACK</p>

</body>
</html>
```